Seeking Creative Website Design for K.R.T Building & Contracting Inc.

Background: K.R.T Building & Contracting Inc., a respected player in the construction and contracting industry, is in urgent need of a modern, efficient website. Our existing website is currently under maintenance due to its outdated design and functionality. We are looking to revamp our online presence with a fresh, professional look that reflects our company's values and expertise.

Website Objective: The primary purpose of our website is to serve as a digital business card for both our current and potential clients. It needs to effectively showcase our services, company ethos, and the high standards of work we deliver.

Key Features:

Modern, User-Friendly Design: A sleek, contemporary design that is easy to navigate. The design should be reflective of our industry and appeal to our client base, which includes major entities like Fuelpoint, QuikNest, and Tarlo.
Service and Contract Request Feature: An integrated feature allowing visitors to submit service or contract requests. These submissions should automatically send an email to info@crewkrt.com.
Company Information: Detailed sections about our services, history, and team. This should include high-quality images and text that communicate our expertise and professionalism.
Contact Information: Clearly displayed contact details, including an email address, phone number, and physical address (418 North Brackwell Commerce Lane, Pontiac MI 48342).
Mobile Responsiveness: The website must be fully functional and visually appealing on both desktop and mobile devices.
SEO Optimization: The site should be optimized for search engines to improve visibility and attract more traffic.
Easy-to-Update: A backend that is simple to update for our team, allowing for regular content refreshes without requiring technical expertise.
What We Are Looking For in a Designer:

Experience and Portfolio: A strong portfolio showcasing your experience, particularly in creating websites for the construction or related industries.
Creativity and Understanding of Our Brand: Someone who can bring innovative ideas to the table while understanding and staying true to the K.R.T Building & Contracting Inc. brand.
Communication and Timeliness: Clear, prompt communication and adherence to project timelines are crucial.
Budget and Timeline:

Budget details and deadline for the project will be discussed further upon contact.
We are excited to see your creative proposals and look forward to establishing a rewarding partnership. Your design could be the cornerstone of our digital identity, helping us connect more effectively with our clients and expand our business.

We need to add this to it as well, "At K.R.T Building & Contracting Inc., we pride ourselves on being more than just a construction company. We are a team of problem solvers, innovators, and craftsmen dedicated to elevating the standards of commercial construction & facility maintenance. Our roots lie in our commitment to quality, reliability, and unparalleled customer service since 1966.

Specializing in a wide array of services, we are known for our expertise in canopy repairs, interior renovations, exterior enhancements, and comprehensive maintenance solutions. From intricate brickwork and robust asphalt paving to delicate interior finishes, we handle every project with precision and a keen eye for detail.

At K.R.T Building & Contracting Inc., we believe in building strong relationships. Our clients trust us for our transparency, adaptability, and ability to deliver exceptional results within stipulated timeframes. Our team, equipped with skilled technicians and seasoned professionals, is the backbone of our success.

Your problem is our solution and our extensive portfolio showcases our versatility and commitment to excellence."

Target Market(s)

Commercial Clients, Potential Employees and Business Owners

Industry/Entity Type

Commercial Construction & Facility Maintenance

Coding

Coded - Design and coding required

Number of Pages Required

5+ page

Font styles to use
Other font styles liked:
• Please see attachment for logo font and colors. Do not want the whole website in the logo font though

Requirements
Nice to have
• A Timeline of our company history, Apply now section, ability to add and remove gallery photos from back end, and maybe a section where we can update our clients on upcoming events, big news, or spotlight type section.

```html
<!DOCTYPE html>
<html lang="en">
<head>
<meta charset="utf-8">
<title>Home — Construction &amp; Facility Maintenance</title>
<link rel="stylesheet" href="https://fonts.googleapis.com/css2?family=Montserrat:wght@400;500;600;700;800&family=Poppins:wght@400;500;600&display=swap">
<style>
:root{
  --stage:#211f2b;
  --blue:#2148a3;
  --blue-soft:#3a5fb8;
  --yellow:#e6e619;
  --ink:#16181d;
  --muted:#8a8f99;
  --white:#ffffff;
  --footer:#1b1e23;
  --line:#e4e6ec;
}
*{box-sizing:border-box;margin:0;padding:0}
html,body{width:1200px;height:1200px;overflow:hidden;background:var(--stage)}
body{font-family:"Poppins",sans-serif;color:var(--ink)}
.page{position:absolute;left:465px;top:78px;width:1000px;height:3860px;background:var(--white);transform:scale(.27);transform-origin:0 0;overflow:hidden}
.abs{position:absolute}
.h{font-family:"Montserrat",sans-serif;font-weight:700}
.center{text-align:center}
.lead{font-size:9px;line-height:17px;color:var(--muted)}
.eyebrow{font-family:"Montserrat",sans-serif;font-size:8px;font-weight:700;letter-spacing:2px;color:var(--blue)}
.sec-title{font-family:"Montserrat",sans-serif;font-weight:700;font-size:27px;color:var(--ink)}
.pill{display:flex;align-items:center;justify-content:center;border-radius:20px;font-family:"Montserrat",sans-serif;font-size:8px;font-weight:700;letter-spacing:1.6px;color:var(--white);background:var(--blue)}
.photo{position:absolute}

/* nav */
.nav{left:0;top:0;width:1000px;height:53px;display:flex;align-items:center}
.brand{position:absolute;left:74px;top:17px;display:flex;align-items:center;gap:6px;font-family:"Montserrat",sans-serif;font-weight:700;font-size:14px;color:var(--blue)}
.brand i{width:12px;height:12px;border-radius:50%;background:var(--blue)}
.menu{position:absolute;left:411px;top:20px;display:flex;gap:30px;font-family:"Montserrat",sans-serif;font-size:8px;letter-spacing:1.6px;font-weight:500;color:#444}
.menu .on{color:var(--blue);font-weight:700}
.nav .pill{position:absolute;left:825px;top:13px;width:138px;height:28px}

/* hero */
.hero{left:0;top:53px;width:1000px;height:460px;background:linear-gradient(100deg,#2a2a2e 0%,#4a4744 40%,#8a8c92 60%,#c86a3c 75%,#9aa3ae 100%)}
.hero-shade{left:0;top:0;width:620px;height:460px;background:linear-gradient(90deg,rgba(0,0,0,.55),rgba(0,0,0,0))}
.hero-title{left:110px;top:158px;font-size:44px;font-weight:800;color:var(--yellow)}
.hero-sub{left:110px;top:218px;font-size:13px;font-weight:600;color:var(--white);font-family:"Montserrat",sans-serif}
.hero-copy{left:110px;top:246px;width:330px;font-size:8.5px;line-height:15px;color:#e8e8e8}
.scroll-word{left:84px;top:320px;writing-mode:vertical-rl;font-family:"Montserrat",sans-serif;font-size:7px;letter-spacing:3px;color:var(--white)}
.scroll-ring{left:72px;top:392px;width:34px;height:34px;border:1px solid rgba(255,255,255,.7);border-radius:50%}
.enquire{left:968px;top:168px;width:32px;height:124px;background:var(--yellow);border-radius:10px 0 0 10px;display:flex;align-items:center;justify-content:center}
.enquire span{writing-mode:vertical-rl;font-family:"Montserrat",sans-serif;font-size:7px;font-weight:700;letter-spacing:2px;color:var(--ink)}

/* about */
.about-feats{left:113px;top:668px;width:790px;display:flex;gap:48px}
.feat{display:flex;gap:14px;width:240px}
.feat-ico{flex:0 0 40px;height:40px;border-radius:50%;background:var(--blue);display:flex;align-items:center;justify-content:center}
.feat-ico.alt{background:var(--yellow)}
.feat h4{font-family:"Montserrat",sans-serif;font-size:13px;font-weight:600;margin:-2px 0 6px}
.feat p{font-size:8px;line-height:15px;color:var(--muted)}

/* why */
.why-img{left:0;top:780px;width:503px;height:337px;background:linear-gradient(120deg,#b9c3cb 0%,#b86a4f 35%,#a5573f 60%,#7c5b4c 100%)}
.why{left:503px;top:780px;width:497px;height:337px;background:var(--blue);color:var(--white)}
.why h2{position:absolute;left:30px;top:32px;font-family:"Montserrat",sans-serif;font-size:25px;font-weight:700}
.why .intro{position:absolute;left:30px;top:70px;width:360px;font-size:9.5px;line-height:16px;font-weight:500}
.why ol{position:absolute;left:30px;top:120px;list-style:none}
.why li{display:flex;gap:10px;align-items:flex-start;margin-bottom:19px;font-size:7.5px;line-height:13px;width:350px;color:#dfe6f5}
.why li b{flex:0 0 24px;height:24px;border-radius:50%;background:var(--white);color:var(--blue);font-size:8px;display:flex;align-items:center;justify-content:center;margin-top:1px}
.why .pill{position:absolute;left:30px;top:275px;width:102px;height:29px;background:var(--yellow);color:var(--ink)}

/* services */
.svc-card{top:1267px;width:222px}
.svc-img{width:222px;height:152px}
.svc-num{margin-top:20px;font-size:8px;font-weight:700;font-family:"Montserrat",sans-serif}
.svc-num:after{content:"";display:block;width:12px;height:3px;background:var(--yellow);margin-top:3px}
.svc-card h3{font-family:"Montserrat",sans-serif;font-size:13px;font-weight:600;margin:12px 0 8px}
.svc-card p{font-size:7.5px;line-height:15px;color:var(--muted)}
.more{margin-top:9px;font-family:"Montserrat",sans-serif;font-size:7.5px;font-weight:700}
.arrow{width:34px;height:34px;border-radius:50%;border:1px solid #c9ccd4;display:flex;align-items:center;justify-content:center}

/* band */
.band{left:0;top:1674px;width:1000px;height:311px;background:var(--blue);color:var(--white)}
.stat{position:absolute;top:48px;width:158px;height:97px;background:var(--blue-soft);text-align:center}
.stat strong{display:block;margin-top:22px;font-family:"Montserrat",sans-serif;font-size:25px;font-weight:800}
.stat span{font-size:7px;color:#d7def0}
.band .sec-title{color:var(--white)}
.band .lead{color:#c9d3ec}
.port{top:1985px;width:250px;height:231px}

/* process */
.tl-line{left:501px;top:2437px;width:2px;height:297px;background:var(--yellow)}
.step-ico{width:40px;height:40px;border-radius:50%;background:var(--blue);display:flex;align-items:center;justify-content:center}
.step h4{font-family:"Montserrat",sans-serif;font-size:13px;font-weight:600;margin-bottom:7px}
.step p{font-size:7.5px;line-height:15px;color:var(--muted);width:175px}
.step.left{text-align:right}
.step.left p{margin-left:auto}

/* reviews */
.rev{top:2935px;width:200px;text-align:center}
.avatar{width:46px;height:46px;border-radius:50%;margin:0 auto 14px;position:relative}
.avatar i{position:absolute;right:-4px;top:-2px;width:13px;height:13px;border-radius:50%;background:#3a86e8;border:2px solid var(--white)}
.rev p{font-size:7px;line-height:12px;color:var(--muted)}
.rev b{display:block;margin-top:10px;font-size:7.5px;line-height:12px;font-weight:600;color:var(--ink)}
.stars{color:#f0b90b;font-size:8px;letter-spacing:1px;margin-top:4px}
.dot{width:26px;height:26px;border-radius:50%;display:flex;align-items:center;justify-content:center;font-size:9px}

/* blog */
.post{top:3257px;width:244px}
.post-img{height:143px}
.post-body{margin:-18px 0 0 44px;background:var(--white);padding:8px 0 0 0}
.meta{display:flex;align-items:center;gap:6px;font-size:6px;color:var(--muted)}
.date{background:var(--yellow);color:var(--ink);font-weight:700;padding:3px 8px;font-size:6px;letter-spacing:1px}
.who{width:12px;height:12px;border-radius:50%;background:#b07c5c}
.post h3{font-family:"Montserrat",sans-serif;font-size:12.5px;font-weight:600;line-height:15px;margin:14px 0 8px}
.post p{font-size:7px;line-height:13px;color:var(--muted)}
.post .go{margin-top:12px;width:22px;height:22px;border-radius:50%;border:1px solid #c9ccd4}

/* footer */
.footer{left:0;top:3660px;width:1000px;height:200px;background:var(--footer);color:var(--white)}
.f-brand{position:absolute;left:68px;top:46px;display:flex;align-items:center;gap:7px;font-family:"Montserrat",sans-serif;font-size:16px;font-weight:700;color:var(--white)}
.f-brand i{width:14px;height:14px;border-radius:50%;background:var(--blue)}
.follow{position:absolute;left:68px;top:98px;font-size:7px;color:#aab}
.socials{position:absolute;left:68px;top:112px;display:flex;gap:5px}
.socials i{width:16px;height:16px;border-radius:50%;background:#3a67d9}
.socials i:last-child{background:#d93a3a}
.contact{position:absolute;top:32px;display:flex;gap:12px;align-items:center}
.c-ico{width:26px;height:26px;border-radius:50%;background:var(--blue);display:flex;align-items:center;justify-content:center}
.contact small{display:block;font-size:6.5px;color:#9aa0ab}
.contact b{font-size:9px;font-weight:600;line-height:12px}
.f-links{position:absolute;left:230px;top:104px;display:flex;gap:28px;font-family:"Montserrat",sans-serif;font-size:7px;letter-spacing:1.5px;color:#aeb3bd}
.copy{position:absolute;left:0;top:150px;width:1000px;text-align:center;font-size:6px;letter-spacing:1.5px;color:#7d838e}
</style>
</head>
<body>
<main class="page">

  <header class="nav abs">
    <div class="brand"><i></i>KRT</div>
    <nav class="menu"><span class="on">HOME</span><span>ABOUT US</span><span>SERVICES ▾</span><span>PORTFOLIO</span><span>CONTACT US</span></nav>
    <div class="pill">REQUEST A QUOTE</div>
  </header>

  <section class="hero abs" role="img" aria-label="Welder in orange overalls repairing a metal canopy with sparks">
    <div class="hero-shade abs"></div>
    <h1 class="hero-title abs h">Canopy Repairs</h1>
    <p class="hero-sub abs">We have everything to build your dream</p>
    <p class="hero-copy abs">Lorem ipsum dolor sit amet consectetur. Quis mollis adipiscing sit tempus auctor sed. Viverra eu nunc sagittis morbi tincidunt. Dui mauris vitae lobortis convallis placerat purus non ipsum.</p>
    <span class="scroll-word abs">SCROLL</span>
    <div class="scroll-ring abs"><svg width="34" height="34" viewBox="0 0 34 34"><path d="M17 11v12M13 19l4 4 4-4" stroke="#fff" fill="none" stroke-width="1.2"/></svg></div>
    <div class="enquire abs"><span>ENQUIRE NOW</span></div>
  </section>

  <section>
    <p class="eyebrow abs center" style="left:0;top:550px;width:1000px">ABOUT US</p>
    <h2 class="sec-title abs center" style="left:0;top:562px;width:1000px">We Are Team KRT</h2>
    <p class="lead abs center" style="left:250px;top:603px;width:500px">Lorem ipsum is simply dummy text of the printing and typesetting industry. Lorem ipsum has been the industry's standard dummy text ever since the 1500s, when an unknown printer took a galley.</p>
    <div class="about-feats abs">
      <div class="feat"><div class="feat-ico"><svg width="16" height="16" viewBox="0 0 16 16"><circle cx="8" cy="5" r="3" fill="#fff"/><path d="M2 15c0-4 3-6 6-6s6 2 6 6z" fill="#fff"/></svg></div><div><h4>Professionals</h4><p>Lorem ipsum dolor sit amet, consectetur adipiscing elit. Eleifend interdum mi faucibus tortor, euismod.</p></div></div>
      <div class="feat"><div class="feat-ico alt"><svg width="16" height="16" viewBox="0 0 16 16"><path d="M8 1l6 2v5c0 4-3 6-6 7-3-1-6-3-6-7V3z" fill="#fff"/></svg></div><div><h4>Trusted</h4><p>Lorem ipsum dolor sit amet, consectetur adipiscing elit. Eleifend interdum mi faucibus tortor, euismod.</p></div></div>
      <div class="feat"><div class="feat-ico"><svg width="16" height="16" viewBox="0 0 16 16"><circle cx="6" cy="6" r="3" fill="#fff"/><path d="M1 15c0-4 2-5 5-5s5 1 5 5z" fill="#fff"/><path d="M12 4v5M10 6.5h4" stroke="#fff" stroke-width="1.4"/></svg></div><div><h4>Expert Designer</h4><p>Lorem ipsum dolor sit amet, consectetur adipiscing elit. Eleifend interdum mi faucibus tortor, euismod.</p></div></div>
    </div>
  </section>

  <div class="photo why-img" role="img" aria-label="Bricklayer in a hard hat building a red brick wall"></div>
  <section class="why abs">
    <h2>Why choose us ?</h2>
    <p class="intro">Lorem ipsum dolor sit amet consectetur. Quis mollis adipiscing sit tempus auctor sed. Viverra eu nunc sagittis morbi tincidunt.</p>
    <ol>
      <li><b>01</b>Lorem ipsum dolor sit amet consectetur adipiscing elit. Eleifend interdum mi faucibus tortor euismod.</li>
      <li><b>02</b>Lorem ipsum dolor sit amet consectetur adipiscing elit. Eleifend interdum mi faucibus tortor euismod.</li>
      <li><b>03</b>Lorem ipsum dolor sit amet consectetur adipiscing elit. Eleifend interdum mi faucibus tortor euismod.</li>
    </ol>
    <div class="pill">KNOW MORE</div>
  </section>

  <section>
    <h2 class="sec-title abs center" style="left:0;top:1160px;width:1000px">Our Services</h2>
    <p class="lead abs center" style="left:250px;top:1200px;width:500px">Lorem ipsum is simply dummy text of the printing and typesetting industry. Lorem ipsum has been the industry's standard dummy text ever since the 1500s, when an unknown printer took a galley.</p>
    <div class="arrow abs" style="left:68px;top:1350px"><svg width="12" height="8" viewBox="0 0 12 8"><path d="M11 4H1M4 1L1 4l3 3" stroke="#333" fill="none"/></svg></div>
    <div class="arrow abs" style="left:898px;top:1350px"><svg width="12" height="8" viewBox="0 0 12 8"><path d="M1 4h10M8 1l3 3-3 3" stroke="#333" fill="none"/></svg></div>
    <article class="svc-card abs" style="left:113px"><div class="svc-img" role="img" aria-label="Modern renovated living room interior" style="background:linear-gradient(160deg,#d9d6d0,#8b8580 55%,#3f3b38)"></div><div class="svc-num">01</div><h3>Interior Renovation</h3><p>Lorem ipsum dolor sit amet, consectetur adipiscing elit. Eleifend interdum mi faucibus tortor, euismod. Adipiscing sed eu posuere at phasellus ipsum urna.</p><div class="more">READ MORE ›</div></article>
    <article class="svc-card abs" style="left:379px"><div class="svc-img" role="img" aria-label="Worker repairing a glass and steel canopy" style="background:linear-gradient(150deg,#cfd8dc,#7c8a93 50%,#b8453a 70%,#dfe5e8)"></div><div class="svc-num">02</div><h3>Canopy Repairs</h3><p>Lorem ipsum dolor sit amet, consectetur adipiscing elit. Eleifend interdum mi faucibus tortor, euismod. Adipiscing sed eu posuere at phasellus ipsum urna.</p><div class="more">READ MORE ›</div></article>
    <article class="svc-card abs" style="left:646px"><div class="svc-img" role="img" aria-label="Building facade with workers on a yellow lift" style="background:linear-gradient(160deg,#f2f2f2,#c9cccf 55%,#d8b020 80%,#e9e9e9)"></div><div class="svc-num">03</div><h3>Exterior Enhancement</h3><p>Lorem ipsum dolor sit amet, consectetur adipiscing elit. Eleifend interdum mi faucibus tortor, euismod. Adipiscing sed eu posuere at phasellus ipsum urna.</p><div class="more">READ MORE ›</div></article>
    <div class="pill abs" style="left:432px;top:1599px;width:137px;height:30px">VIEW ALL SERVICES</div>
  </section>

  <section class="band abs">
    <div class="stat" style="left:168px"><strong>701</strong><span>Completed Project</span></div>
    <div class="stat" style="left:338px"><strong>1234</strong><span>Worldwide Client</span></div>
    <div class="stat" style="left:508px"><strong>1275</strong><span>Experience Worker</span></div>
    <div class="stat" style="left:678px"><strong>49</strong><span>Total Awards</span></div>
    <h2 class="sec-title abs center" style="left:0;top:193px;width:1000px">Our Portfolio</h2>
    <p class="lead abs center" style="left:250px;top:235px;width:500px">Lorem ipsum is simply dummy text of the printing and typesetting industry. Lorem ipsum has been the industry's standard dummy text ever since the 1500s, when an unknown printer took a galley.</p>
  </section>
  <div class="photo port" style="left:0;background:linear-gradient(150deg,#dfe7ef,#5a83c0 50%,#c9a070 75%,#e8e6e0)" role="img" aria-label="Two engineers in hard hats reviewing plans on site"></div>
  <div class="photo port" style="left:250px;background:var(--yellow);display:flex;flex-direction:column;align-items:center;justify-content:center" role="img" aria-label="Bathroom and interior design project with yellow overlay"><span class="h" style="font-size:8px;letter-spacing:1px">BATHROOMS, BATHS</span><span style="font-size:7px">AND INTERIOR DESIGN</span></div>
  <div class="photo port" style="left:500px;background:linear-gradient(160deg,#f1f1ef,#c9c4ba 50%,#4a6aa8 75%,#ece9e3)" role="img" aria-label="Workers installing drywall in an interior"></div>
  <div class="photo port" style="left:750px;background:linear-gradient(160deg,#e9edf0,#8a5a3a 45%,#3a3430 75%,#c9c2b6)" role="img" aria-label="Modern house exterior with wood and stone cladding"></div>
  <div class="pill abs" style="left:432px;top:2237px;width:137px;height:30px">GET A QUOTE</div>

  <section>
    <p class="eyebrow abs center" style="left:0;top:2318px;width:1000px">HOW WE WORK</p>
    <h2 class="sec-title abs center" style="left:0;top:2330px;width:1000px">Our Process</h2>
    <p class="lead abs center" style="left:250px;top:2372px;width:500px">Lorem ipsum is simply dummy text of the printing and typesetting industry. Lorem ipsum has been the industry's standard dummy text ever since the 1500s, when an unknown printer took a galley.</p>
    <div class="tl-line abs"></div>
    <div class="step-ico abs" style="left:527px;top:2425px"><svg width="16" height="16" viewBox="0 0 16 16"><path d="M8 2a4 4 0 0 0-2 7.5V11h4V9.5A4 4 0 0 0 8 2zM6 13h4" stroke="#fff" fill="none" stroke-width="1.2"/></svg></div>
    <div class="step abs" style="left:593px;top:2424px"><h4>First we create idea</h4><p>Lorem ipsum dolor sit amet, consectetur adipiscing elit. Eleifend interdum mi faucibus tortor, euismod.</p></div>
    <div class="step-ico abs" style="left:435px;top:2518px"><svg width="16" height="16" viewBox="0 0 16 16"><rect x="2" y="3" width="11" height="11" stroke="#fff" fill="none" stroke-width="1.2"/><path d="M5 11l8-8" stroke="#fff" stroke-width="1.2"/></svg></div>
    <div class="step left abs" style="left:210px;top:2517px;width:199px"><h4>After we create sketch</h4><p>Lorem ipsum dolor sit amet, consectetur adipiscing elit. Eleifend interdum mi faucibus tortor, euismod.</p></div>
    <div class="step-ico abs" style="left:527px;top:2611px"><svg width="16" height="16" viewBox="0 0 16 16"><circle cx="8" cy="8" r="5" stroke="#fff" fill="none" stroke-width="1.2"/><path d="M3 13l10-10" stroke="#fff" stroke-width="1.2"/></svg></div>
    <div class="step abs" style="left:593px;top:2610px"><h4>Create the design</h4><p>Lorem ipsum dolor sit amet, consectetur adipiscing elit. Eleifend interdum mi faucibus tortor, euismod.</p></div>
    <div class="step-ico abs" style="left:435px;top:2705px"><svg width="16" height="16" viewBox="0 0 16 16"><path d="M2 14h12M4 14V8h3v6M9 14V4h3v10" stroke="#fff" fill="none" stroke-width="1.2"/></svg></div>
    <div class="step left abs" style="left:210px;top:2707px;width:199px"><h4>Build and publish</h4><p>Lorem ipsum dolor sit amet, consectetur adipiscing elit. Eleifend interdum mi faucibus tortor, euismod.</p></div>
  </section>

  <section>
    <div class="abs" role="img" aria-label="Faint dotted world map background" style="left:160px;top:2830px;width:680px;height:330px;background:radial-gradient(ellipse at center,#f3f4f7,#ffffff 70%)"></div>
    <h2 class="sec-title abs center" style="left:0;top:2848px;width:1000px">Our Client’s Reviews</h2>
    <div class="rev abs" style="left:153px"><div class="avatar" role="img" aria-label="Client portrait" style="background:#a8453a"><i></i></div><p>Amazing, quick turnaround time helps to establish clarity by the candidate</p><b>Recruitment manager,<br>IT services provider</b><div class="stars">★★★★★</div></div>
    <div class="rev abs" style="left:408px"><div class="avatar" role="img" aria-label="Client portrait" style="background:#e2b07a"><i></i></div><p>Comprehensive report with auditable evidence... meets the purpose</p><b>Head of compliance, top leading IT<br>services organization</b><div class="stars">★★★★★</div></div>
    <div class="rev abs" style="left:663px"><div class="avatar" role="img" aria-label="Client portrait" style="background:#e8c330"><i></i></div><p>Good solution......data helps to negotiate salary</p><b>Head HR, leading<br>BPO organization</b><div class="stars">★★★★★</div></div>
    <div class="dot abs" style="left:467px;top:3108px;background:#fff;box-shadow:0 2px 6px rgba(0,0,0,.15)">←</div>
    <div class="dot abs" style="left:506px;top:3108px;background:var(--blue);color:#fff">→</div>
  </section>

  <section>
    <h2 class="sec-title abs center" style="left:0;top:3190px;width:1000px">Latest From The Blog</h2>
    <article class="post abs" style="left:113px"><div class="post-img" role="img" aria-label="Worker installing a glass canopy roof" style="background:linear-gradient(160deg,#eef3e6,#b8c9a6 50%,#7a8a80)"></div><div class="post-body"><div class="meta"><span class="date">20 NOV, 2023</span><span class="who"></span>by admin doe</div><h3>Lorem ipsum dolor sit amet consectetur.</h3><p>Lorem ipsum dolor sit amet consectetur. Donec lectus nunc risus morbi dui. Fringilla interdum eu consectetur in mi.</p><div class="go"></div></div></article>
    <article class="post abs" style="left:379px"><div class="post-img" role="img" aria-label="Interior renovation of a room under construction" style="background:linear-gradient(160deg,#d8d2c8,#8e8378 50%,#c8beb0)"></div><div class="post-body"><div class="meta"><span class="date">20 NOV, 2023</span><span class="who"></span>by admin doe</div><h3>Lorem ipsum dolor sit amet consectetur.</h3><p>Lorem ipsum dolor sit amet consectetur. Donec lectus nunc risus morbi dui. Fringilla interdum eu consectetur in mi.</p><div class="go"></div></div></article>
    <article class="post abs" style="left:646px"><div class="post-img" role="img" aria-label="Worker installing a glass canopy roof" style="background:linear-gradient(160deg,#eef3e6,#b8c9a6 50%,#7a8a80)"></div><div class="post-body"><div class="meta"><span class="date">20 NOV, 2023</span><span class="who"></span>by admin doe</div><h3>Lorem ipsum dolor sit amet consectetur.</h3><p>Lorem ipsum dolor sit amet consectetur. Donec lectus nunc risus morbi dui. Fringilla interdum eu consectetur in mi.</p><div class="go"></div></div></article>
    <div class="pill abs" style="left:446px;top:3577px;width:110px;height:30px">VIEW ALL</div>
  </section>

  <footer class="footer abs">
    <div class="f-brand"><i></i>KRT</div>
    <div class="follow">Follow us</div>
    <div class="socials"><i></i><i></i><i></i></div>
    <div class="contact" style="left:231px"><div class="c-ico"><svg width="10" height="12" viewBox="0 0 10 12"><path d="M5 11S1 7 1 4.5a4 4 0 0 1 8 0C9 7 5 11 5 11z" fill="#fff"/><circle cx="5" cy="4.5" r="1.4" fill="#2148a3"/></svg></div><div><small>Office Location</small><b>XX dummy address,<br>PA XXXX</b></div></div>
    <div class="contact" style="left:518px"><div class="c-ico"><svg width="11" height="11" viewBox="0 0 11 11"><path d="M2 1h2l1 3-1.5 1a6 6 0 0 0 2.5 2.5L7 6l3 1v2a1 1 0 0 1-1 1A9 9 0 0 1 1 2a1 1 0 0 1 1-1z" fill="#fff"/></svg></div><div><small>Call us Monday - Friday</small><b>+X XXX XXXX XXXX</b></div></div>
    <div class="contact" style="left:785px"><div class="c-ico"><svg width="11" height="9" viewBox="0 0 11 9"><rect x="0.5" y="0.5" width="10" height="8" fill="#fff"/><path d="M1 1l4.5 4L10 1" stroke="#2148a3" fill="none"/></svg></div><div><small>E-Mail us</small><b>info@example.com</b></div></div>
    <nav class="f-links"><span>HOME</span><span>ABOUT US</span><span>SERVICES</span><span>PORTFOLIO</span><span>BLOGS</span><span>CONTACT US</span><span>PRIVACY POLICY</span><span>TERMS &amp; CONDITIONS</span></nav>
    <p class="copy">COPYRIGHT © 2023. ALL RIGHTS RESERVED</p>
  </footer>

</main>
</body>
</html>
```